Auto glass company

THRIFTWAY
Roving Auto Glass, LLC
555-604-1973

* Windshield Replacement
* Rock Chip Repair
Danny "K"
Thriftwayrovingautoglass@mailbox-demo.net
* Fully Insured

This is what I would like on the card. The image is what I had before. Looking for a logo possible too, couldn’t find a place to add that on. It’s a auto glass company.

Target Market(s)

Auto glass

Industry/Entity Type

Auto glass

Contact Information for Business Card

Logo, business name, phone number, windshield replacement, rock chip repair, insured, owner name Danny K, email address thriftwayrovingautoglass@mailbox-demo.net

Colors

Designer to choose colors to be used in the design.

Requirements
Must have
• Logo, business name, phone number, windshield replacement, rock chip repair, insured, owner name Danny K, email address thriftwayrovingautoglass@mailbox-demo.net

```html
<!DOCTYPE html>
<html lang="en">
<head>
<meta charset="utf-8">
<title>Thriftway Roving Auto Glass – Business Card</title>
<link rel="stylesheet" href="https://fonts.googleapis.com/css2?family=Tenor+Sans&family=Mulish:wght@400;700&display=swap">
<style>
  :root {
    --backdrop: #d8d2c8;
    --card: #1f1e1f;
    --card-edge: #2a292a;
    --accent: #5cc6f0;
    --text-light: #f2f2f2;
    --name-silver: #c9ccd1;
  }
  * { box-sizing: border-box; margin: 0; padding: 0; }
  html, body {
    width: 1200px; height: 900px; overflow: hidden;
    background: var(--backdrop);
  }
  .sheet {
    width: 1200px; height: 900px;
    display: flex; flex-direction: column; align-items: center; justify-content: center;
    gap: 44px;
  }
  .card {
    position: relative;
    width: 700px; height: 400px;
    background: var(--card);
    border-radius: 44px;
    box-shadow: 0 10px 28px rgba(0,0,0,.28), inset 0 0 0 1px var(--card-edge);
    color: var(--text-light);
    font-family: "Tenor Sans", "Mulish", sans-serif;
  }
  .brand {
    position: absolute; left: 56px; top: 54px;
    display: flex; align-items: center; gap: 16px;
    color: var(--name-silver);
  }
  .brand-dot {
    width: 18px; height: 18px; border-radius: 50%;
    background: var(--accent);
    flex: none;
  }
  .brand-text { line-height: 1.15; }
  .brand-name { display: block; font-size: 42px; letter-spacing: 2px; }
  .brand-sub  { display: block; font-size: 17px; letter-spacing: 3px; }

  .services {
    position: absolute; right: 52px; bottom: 62px;
    list-style: none; text-align: right;
    font-size: 21px; line-height: 1.55;
  }
  .services li::after {
    content: ""; display: inline-block;
    width: 10px; height: 10px; border-radius: 50%;
    background: var(--accent);
    margin-left: 12px; vertical-align: 5px;
  }

  .contact {
    position: absolute; right: 40px; bottom: 58px;
    border-left: 2px solid var(--accent);
    padding: 6px 0 10px 26px;
  }
  .contact-name {
    font-family: "Mulish", sans-serif; font-weight: 700;
    color: var(--accent); font-size: 30px; margin-bottom: 12px;
  }
  .contact-line {
    display: flex; align-items: center; gap: 12px;
    font-size: 19px; line-height: 1.6;
  }
  .contact-line svg { width: 18px; height: 18px; flex: none; }
</style>
</head>
<body>
<main class="sheet">

  <section class="card card-front">
    <div class="brand">
      <span class="brand-dot"></span>
      <div class="brand-text">
        <span class="brand-name">THRIFTWAY</span>
        <span class="brand-sub">Roving Auto Glass, LLC</span>
      </div>
    </div>
    <ul class="services">
      <li>Fully Insured</li>
      <li>Rock Chip Repair</li>
      <li>Windshield Replacement</li>
    </ul>
  </section>

  <section class="card card-back">
    <div class="brand">
      <span class="brand-dot"></span>
      <div class="brand-text">
        <span class="brand-name">THRIFTWAY</span>
        <span class="brand-sub">Roving Auto Glass, LLC</span>
      </div>
    </div>
    <div class="contact">
      <p class="contact-name">Danny "K"</p>
      <p class="contact-line">
        <svg viewBox="0 0 18 18" aria-hidden="true"><rect x="4.5" y="1" width="9" height="16" rx="1.5" fill="none" stroke="#5cc6f0" stroke-width="1.6"/><line x1="7.5" y1="14.2" x2="10.5" y2="14.2" stroke="#5cc6f0" stroke-width="1.4"/></svg>
        555-604-1973
      </p>
      <p class="contact-line">
        <svg viewBox="0 0 18 18" aria-hidden="true"><rect x="1" y="4" width="16" height="11" rx="1.5" fill="#5cc6f0"/><polyline points="1.5,4.8 9,10.5 16.5,4.8" fill="none" stroke="#1f1e1f" stroke-width="1.5"/></svg>
        thriftwayrovingautoglass@mailbox-demo.net
      </p>
    </div>
  </section>

</main>
</body>
</html>
```